New website for salon services and wedding hair and makeup

I am a professional hairstylist and makeup artist in Charleston, SC. I have my own company where I see clients for cut and color and I also go on site for weddings. I have a current website that I would like to update and change the style. I would like to add a contact form, map, additional pages and be mobile friendly. It is important to me that it have a site map and can show up in searches. I will need to add photos to the site every so often and would like to continue to work with the designer. I have a logo that I am happy with and have attached the file however if you think a new logo would help the look of the site I am open to it. My current website is www.brindlecrestbeauty.com, I would like to change the style and layout so it looks up to date. Here are some links to sites that I like the look of but I don't want to limit your creativity. http://copperwillowlane.com/ http://www.glintmorrowstudio.com http://marisqueldon.com/. I have attached a few files for mock up purposes, please let me know if you would like more content. Thank you!

Target Market(s)

Women, Brides

Industry/Entity Type

Hair And Beauty

Number of Pages Required

1 page

Font styles to use
Sans Serif
Script

Requirements
Must have
• Contact form, Mobile friendly, sitemap
Nice to have
• I really like the look for the sites I have included on the project description guide.
Should not have
• Nothing overly girly.

```html
<!DOCTYPE html>
<html lang="en">
<head>
<meta charset="utf-8">
<title>Brindlecrest Hair and Makeup</title>
<link rel="stylesheet" href="https://fonts.googleapis.com/css2?family=Bebas+Neue&family=Great+Vibes&family=Open+Sans:wght@400;600;700&family=Raleway:wght@400;600&display=swap">
<style>
:root{
  --navy:#0e3556;
  --navy-dark:#0a2a45;
  --tab-active:#2a6f9c;
  --ink:#1c3d5e;
  --text:#5b6670;
  --line:#1c3d5e;
  --paper:#ffffff;
  --wood:#e9eaec;
  --teal:#7fd0d8;
  --violet:#6a2b8e;
  --field:#ffffff;
  --field-border:#9aa6b2;
}
*{margin:0;padding:0;box-sizing:border-box}
html,body{width:1200px;height:3512px;overflow:hidden;background:var(--paper)}
body{position:relative;font-family:"Open Sans",sans-serif;color:var(--text)}
.abs{position:absolute}

/* Hero */
.hero{left:0;top:0;width:1200px;height:800px;background:linear-gradient(180deg,#f1f2f4 0%,var(--wood) 100%)}
.hero-photo{left:560px;top:0;width:640px;height:800px;background:linear-gradient(160deg,#cfd2d6 0%,#8c8f94 45%,#e6e2dc 100%)}
.hero-ribbon{left:760px;top:640px;width:440px;height:120px;background:linear-gradient(90deg,var(--violet),#9b55c0);border-radius:60px 0 0 60px;opacity:.9}
.brand{left:80px;top:70px;display:flex;align-items:center;gap:16px}
.brand-dot{width:60px;height:60px;border-radius:50%;background:var(--teal)}
.brand-name{font-family:"Raleway",sans-serif;font-weight:600;font-size:34px;color:var(--ink)}
.tagline{left:100px;top:320px;font-family:"Bebas Neue",sans-serif;font-size:104px;line-height:108px;color:var(--ink);letter-spacing:3px}

/* Nav */
.nav{left:0;top:800px;width:1200px;height:70px;background:var(--navy);display:flex;padding-left:80px}
.nav a{font-family:"Raleway",sans-serif;font-size:20px;color:#fff;text-decoration:none;padding:0 56px;line-height:70px;letter-spacing:1px}
.nav a.active{background:var(--tab-active)}

/* About */
.about-photo{left:140px;top:970px;width:360px;height:520px;background:linear-gradient(180deg,#b7c7d6 0%,#7d8f9e 55%,#c9b9a4 100%)}
.welcome{left:600px;top:900px;font-family:"Great Vibes",cursive;font-size:64px;color:var(--ink)}
.about-title{left:600px;top:970px;font-family:"Bebas Neue",sans-serif;font-size:72px;color:var(--ink);letter-spacing:2px}
.about-copy{left:600px;top:1060px;width:520px;font-size:14.5px;line-height:22px}
.about-copy p{margin-bottom:20px}

.divider{left:0;width:1200px;height:4px;background:var(--line)}
.section-title{left:80px;font-family:"Bebas Neue",sans-serif;font-size:88px;color:var(--ink);letter-spacing:3px}

/* Gallery */
.gallery-item{top:1680px;height:160px}
.arrow{top:1735px}

/* Services */
.service{top:2040px;width:240px;text-align:center}
.service-photo{width:200px;height:200px;margin:0 auto;border-radius:50%;border:4px solid var(--navy)}
.service h3{font-family:"Raleway",sans-serif;font-weight:600;font-size:26px;color:var(--ink);margin:24px 0 14px}
.service p{font-size:14px;line-height:21px}
.service .note{color:var(--tab-active);margin-top:2px}
.extensions{left:0;top:2540px;width:1200px;text-align:center;font-family:"Raleway",sans-serif;font-weight:600;font-size:26px;color:var(--ink)}

/* Contact */
.contact-info{left:80px;top:2780px;width:420px;font-size:15px;line-height:24px}
.contact-info p{margin-bottom:20px}
.contact-line{display:flex;align-items:center;gap:16px;margin-bottom:18px;color:var(--ink)}
.social{display:flex;gap:20px;margin-top:26px}
.social span{width:40px;height:40px;background:var(--navy);display:block}
.contact-form{left:600px;top:2780px;width:520px;display:grid;grid-template-columns:1fr 1fr;gap:22px 40px}
.field{height:40px;border:2px solid var(--field-border);background:var(--field);font-size:14px;color:#8a949e;padding:9px 12px}
.field.wide{grid-column:1/3;height:150px}
.submit{width:150px;height:46px;background:var(--navy);color:#fff;font-family:"Raleway",sans-serif;font-weight:600;font-size:17px;letter-spacing:1px;display:flex;align-items:center;justify-content:center}

/* Map & footer */
.map{left:0;top:3120px;width:1200px;height:300px;background:linear-gradient(135deg,#d9e4d0 0%,#c3d7e6 50%,#a9c6df 100%)}
.footer{left:0;top:3420px;width:1200px;height:92px;background:var(--navy-dark);text-align:center;color:#fff}
.footer-links{padding-top:18px;display:flex;justify-content:center;gap:50px;font-family:"Raleway",sans-serif;font-size:16px}
.copyright{margin-top:14px;font-size:14px}
.copyright strong{font-weight:700}
</style>
</head>
<body>

<header class="abs hero">
  <div class="abs hero-photo" role="img" aria-label="Bride and groom posing in formal wedding attire"></div>
  <div class="abs hero-ribbon" role="img" aria-label="Purple satin ribbon with lavender sprigs"></div>
  <div class="abs brand"><span class="brand-dot"></span><span class="brand-name">Brindlecrest Hair and Makeup</span></div>
  <h1 class="abs tagline">Chic<br>Sophisticate<br>Dinspired</h1>
</header>

<nav class="abs nav">
  <a class="active">ABOUT</a><a>GALLERY</a><a>SERVICES</a><a>CONTACT</a>
</nav>

<section class="about">
  <div class="abs about-photo" role="img" aria-label="Wedding couple embracing on the beach near a pier"></div>
  <div class="abs welcome">Welcome</div>
  <h2 class="abs about-title">Brindlecrest</h2>
  <div class="abs about-copy">
    <p>Brindlecrest Hair and Makeup specializes in providing gorgeous, long lasting hair and makeup. With over nine years of experience and training, we know how to make your day the very best. We take pride in client satisfaction and helping you achieve the look of your dreams while making the experience memorable and enjoyable. We work on location so you can relax and share your day with the people you love. We only use the highest quality products, allowing you to dance the night away while your hair and makeup remain flawless. From traditional makeup, airbrush and hair extensions, we will tailor a custom look just for you!</p>
    <p>If your needs are of a more professional nature we have you covered! Brindlecrest also specializes in airbrush makeup for high definition film, photo shoots, and runway. Our hairstylists specialize in cut, color and extensions giving your client the look they want.</p>
    <p>We also provide services in studio and are happy to meet all of your hair care needs.</p>
  </div>
</section>

<div class="abs divider" style="top:1550px"></div>

<section class="gallery">
  <h2 class="abs section-title" style="top:1575px">Gallery</h2>
  <svg class="abs arrow" style="left:36px" width="24" height="50" viewBox="0 0 24 50"><path d="M20 4 L4 25 L20 46" fill="none" stroke="#1c3d5e" stroke-width="4"/></svg>
  <div class="abs gallery-item" style="left:80px;width:230px;background:linear-gradient(135deg,#e8d2c2,#b08b76)" role="img" aria-label="Bride having her hair styled"></div>
  <div class="abs gallery-item" style="left:350px;width:220px;background:linear-gradient(135deg,#efe3cf,#c9a882)" role="img" aria-label="Bridal updo with soft curls"></div>
  <div class="abs gallery-item" style="left:620px;width:220px;background:linear-gradient(135deg,#9a9a9a,#3e3e3e)" role="img" aria-label="Black and white wedding ceremony moment"></div>
  <div class="abs gallery-item" style="left:880px;width:240px;background:linear-gradient(180deg,#a9c1d6,#d8c9b3)" role="img" aria-label="Couple on the beach at sunset"></div>
  <svg class="abs arrow" style="left:1140px" width="24" height="50" viewBox="0 0 24 50"><path d="M4 4 L20 25 L4 46" fill="none" stroke="#1c3d5e" stroke-width="4"/></svg>
</section>

<div class="abs divider" style="top:1910px"></div>

<section class="services">
  <h2 class="abs section-title" style="top:1935px">Our Services</h2>
  <div class="abs service" style="left:85px">
    <div class="service-photo" style="background:linear-gradient(135deg,#f0e6dc,#c7ab92)" role="img" aria-label="Bride with elegant hairstyle"></div>
    <h3>Bridal</h3>
    <p>Thank you for your interest in our on location bridal services. Please contact us for more information.</p>
  </div>
  <div class="abs service" style="left:290px">
    <div class="service-photo" style="background:linear-gradient(135deg,#8f8f8f,#2f2f2f)" role="img" aria-label="Man with a modern haircut"></div>
    <h3>Hair Cut</h3>
    <p>Women $35<br>Men $20</p>
  </div>
  <div class="abs service" style="left:520px">
    <div class="service-photo" style="background:linear-gradient(135deg,#d8497a,#6b3fa0,#3d9bd6)" role="img" aria-label="Vivid multicolored hair"></div>
    <h3>Color</h3>
    <p>Partial Highlights $130+<br>Full Highlights $165+<br>Double Process $155+<br>Ombré $125+<br>Roots with Gloss $110+<br>All Over Color $120+</p>
    <p class="note">All color services include a complimentary hair cut and blowout</p>
  </div>
  <div class="abs service" style="left:780px">
    <div class="service-photo" style="background:linear-gradient(135deg,#f3dcb0,#c9904f)" role="img" aria-label="Woman with styled blonde waves"></div>
    <h3>Styling &amp; Treatments</h3>
    <p>Blow-out/Hair Styling $35<br>Event Updo $85<br>Deep Condition $15<br>Keratin Smoothing Treatment $150+</p>
  </div>
  <div class="abs extensions">Hair Extensions – Complimentary Consultation</div>
</section>

<div class="abs divider" style="top:2630px"></div>

<section class="contact">
  <h2 class="abs section-title" style="top:2655px">Contact Us</h2>
  <div class="abs contact-info">
    <p>Have a question, desire more information, or just want to have a chat?</p>
    <p>Please contact us:</p>
    <div class="contact-line">
      <svg width="22" height="22" viewBox="0 0 24 24"><path d="M6.6 10.8a15 15 0 0 0 6.6 6.6l2.2-2.2a1 1 0 0 1 1-.25 11.4 11.4 0 0 0 3.6.57 1 1 0 0 1 1 1V20a1 1 0 0 1-1 1A17 17 0 0 1 3 4a1 1 0 0 1 1-1h3.5a1 1 0 0 1 1 1c0 1.25.2 2.45.57 3.57a1 1 0 0 1-.25 1z" fill="#0e3556"/></svg>
      <span>843.555.0172</span>
    </div>
    <div class="contact-line">
      <svg width="22" height="22" viewBox="0 0 24 24"><rect x="2" y="5" width="20" height="14" rx="2" fill="none" stroke="#0e3556" stroke-width="2"/><path d="M2 6l10 7 10-7" fill="none" stroke="#0e3556" stroke-width="2"/></svg>
      <span>hello@brindlecrestbeauty.com</span>
    </div>
    <p>We look forward to hearing from you!</p>
    <div class="social"><span></span><span></span><span></span></div>
  </div>
  <form class="abs contact-form">
    <div class="field">Enter Name</div>
    <div class="field">Enter Email</div>
    <div class="field">Enter Contact No.</div>
    <div class="field">Enter Subject</div>
    <div class="field wide">Message</div>
    <div class="submit">SUBMIT</div>
  </form>
</section>

<div class="abs map" role="img" aria-label="Map of the Charleston, SC area"></div>

<footer class="abs footer">
  <div class="footer-links"><span>HOME</span><span>ABOUT</span><span>GALLERY</span><span>SERVICES</span><span>CONTACT</span></div>
  <div class="copyright">© <strong>Brindlecrest Hair and Makeup</strong>. 2015. All Rights Reserved.</div>
</footer>

</body>
</html>
```